Unique Alcoholic Beverage (Beer Ice!) needs Exciting Package Design

We need a package designed for Quorvel Beer Ice, an alcoholic flavored ice that is added to beer to keep it ice-cold and enhance the taste. Specifically we need graphics for shrink wrap designed to shrink 3 containers together, and graphics for a foil lid used to seal the containers that are shrink wrapped together.

The final design should communicate a fun and relaxed feel that fits with relaxed outdoor beer drinking, either at an outdoor event or simply relaxing outside with friends. See attachments and their descriptions below for more detail.

Attachments:
DESIGN REQUIREMENTS – this folder contains all of the specific design requirements, mostly contained within the word file.

DESIGN INSPIRATION – this folder contains examples of designs that appeal to us

LOGOS – this folder contains various examples of our current logo. We like our current logo but feel free to change it if you think it will make your overall design better. We are not locked in to the logo just yet.

PRODUCT EXAMPLES – this folder contains examples of the product itself to help you understand how it works and how it is packaged. In short, the product is packaged in what looks like a yogurt container with a foil lid. 3 “yogurt” containers are then stacked on top of each other and shrink wrapped together. You are designing the foil lid and the outer shrink wrap. Examples of the lid, the shrink wrap, and the product itself are in the “Product Examples” folder and described below:

Lid Example – a 3D rendering of the cup/lid combination. This in no way reflects what we are looking for design wise, it is only meant to help visualize the shape of the container. Note that the “cup” portion of this will be plain white, so we want the lid to really stand out and give the container some personality.

Shrink Examples (2) – this example is 4 wine glasses shrink wrapped together. We will be doing 3 “yogurt” cups instead of 4 wine glasses. Again, this is not meant to show what we are looking for graphic design wise, only to help you visualize the overall packaging shape.

Product Examples (2) - Including some pictures of the "beer ice" in use so you can get a sense of how the consumer will ultimately use the product. We want the consumer to immediately understand how to use it from the packaging.
Updates

Project Deadline Extended
Reason: Need additional time to review submissions. There will be no more extensions. Thanks!

Target Market(s)

Beer drinkers aged 25-45

Requirements
Must have
• - See design requirement folder attached. Note that the government requires all wording where we say "Must have". We would recommend using all the additional "recommended" wording we provide as well.
• Additional requirements:
• - Deliverable in Adobe Illustrator files
• - Designs for all 3 flavors (Lemon Shandy, Lime, Strawberry)
• - Designs for both the shrink wrap and the foil lids
Nice to have
• See design inspirations folder. We are looking for "simple with subtle details". We also want something that helps people "get it" immediately. Something that quickly conveys that this is ice meant to be put in a beer would be helpful.
Should not have
• No health benefit claims or anything targeted towards individuals under the age of 21.
• Seeing a lot of ice cubes incorporated into the designs. We want the packaging to project cold and refreshing, but ice cubes made of water suggest the product will water your beer down (it does not, since it is fruit flavored!). Would recommend avoiding water/ice cubes in the picture. Refreshing, fruity, and cold is what we want, just not watery. Thanks!

```html
<!DOCTYPE html>
<html lang="en">
<head>
<meta charset="utf-8">
<title>Quorvel Beer Ice – Lemon Flavor Ice Shrink Wrap</title>
<link rel="stylesheet" href="https://fonts.googleapis.com/css2?family=Montserrat:wght@700;800&family=Open+Sans:wght@600&family=Oswald:wght@300;400&display=swap">
<style>
  :root {
    --grey: #bbbdc0;
    --mint: #bfe3d9;
    --sun: #f5c157;
    --sky: #5ec8e5;
    --ink: #231f20;
    --lime: #bed632;
    --maroon: #5a2d3c;
    --crimson: #a8234a;
    --tangerine: #e35f34;
    --white: #ffffff;
  }
  html, body {
    margin: 0;
    padding: 0;
    overflow: hidden;
  }
  .wrap-panel {
    position: relative;
    width: 1200px;
    height: 698px;
    background: var(--grey);
    overflow: hidden;
  }
  .backdrop, .emblem {
    position: absolute;
    left: 0;
    top: 0;
  }
  .product-title {
    position: absolute;
    top: 8px;
    left: 0;
    width: 1184px;
    margin: 0;
    text-align: center;
    font-family: "Montserrat", sans-serif;
    font-weight: 800;
    font-size: 114px;
    letter-spacing: 6px;
    line-height: 1;
    color: var(--sky);
    -webkit-text-stroke: 7px var(--ink);
    paint-order: stroke fill;
  }
  .brand-name {
    position: absolute;
    left: 437px;
    top: 362px;
    width: 320px;
    text-align: center;
    font-family: "Montserrat", sans-serif;
    font-weight: 800;
    font-size: 50px;
    letter-spacing: 2px;
    line-height: 1;
    color: var(--white);
  }
  .flavor-label {
    position: absolute;
    left: 382px;
    top: 603px;
    width: 438px;
    height: 52px;
    margin: 0;
    background: var(--ink);
    color: var(--lime);
    font-family: "Open Sans", sans-serif;
    font-weight: 600;
    font-size: 39px;
    line-height: 52px;
    text-align: center;
  }
  .health-warning {
    position: absolute;
    left: 96px;
    top: 601px;
    width: 278px;
    margin: 0;
    font-family: "Oswald", sans-serif;
    font-weight: 300;
    font-size: 10.5px;
    line-height: 13px;
    color: var(--ink);
  }
  .usage-steps {
    position: absolute;
    left: 832px;
    top: 247px;
    width: 490px;
    height: 170px;
    margin: 0;
    padding: 0 0 0 14px;
    box-sizing: border-box;
    transform: rotate(-90deg);
    transform-origin: center;
    font-family: "Oswald", sans-serif;
    font-weight: 300;
    font-size: 12.5px;
    line-height: 21px;
    color: var(--ink);
    list-style: disc;
  }
  .usage-steps li {
    margin: 0;
  }
</style>
</head>
<body>
<main class="wrap-panel">
  <svg class="backdrop" width="1200" height="698" viewBox="0 0 1200 698" aria-hidden="true">
    <path class="wave wave--mint-left" fill="var(--mint)" d="M0,0 H265 C235,110 175,200 162,300 C150,420 60,520 72,698 H0 Z"/>
    <path class="drop drop--sun-left" fill="var(--sun)" d="M245,290 C252,380 382,470 386,600 L386,698 H80 C62,560 150,470 190,400 C222,350 242,320 245,290 Z"/>
    <path class="wave wave--sun-right" fill="var(--sun)" d="M930,0 H1200 V698 H1085 C1092,560 1012,460 988,360 C968,280 935,200 930,0 Z"/>
    <path class="drop drop--mint-right" fill="var(--mint)" d="M955,300 C962,400 1082,470 1086,600 V698 H830 C836,560 900,470 930,400 C948,360 955,330 955,300 Z"/>
  </svg>

  <h1 class="product-title">BEER ICE</h1>

  <svg class="emblem" width="1200" height="698" viewBox="0 0 1200 698">
    <defs>
      <radialGradient id="bloom-tones" cx="50%" cy="50%" r="50%">
        <stop offset="0%" stop-color="var(--crimson)"/>
        <stop offset="60%" stop-color="var(--tangerine)"/>
        <stop offset="100%" stop-color="var(--lime)"/>
      </radialGradient>
    </defs>
    <circle class="bloom-ornament" cx="597" cy="390" r="250" fill="url(#bloom-tones)" opacity="0.85" role="img" aria-label="Decorative ring of colourful fruit-toned petals behind the brand mark"/>
    <circle class="brand-disc" cx="597" cy="390" r="160" fill="var(--ink)" aria-hidden="true"/>
  </svg>

  <div class="brand-name">QUORVEL</div>

  <h2 class="flavor-label">LEMON FLAVOR ICE</h2>

  <p class="health-warning">WARNING: According to the Surgeon General, women should not drink alcoholic beverages during pregnancy because of the risk of birth defects. Consumption of alcoholic beverages impairs your ability to drive a car or operate machinery, and may cause health problems.</p>

  <ul class="usage-steps">
    <li>Freeze in your freezer overnight. If you're in a rush a few hours will do the trick if you don't mind the ice melting faster (also flavors your beer faster).</li>
    <li>Drop Quorvel into your favorite beer. Or get creative and try them in all kinds of beverages! We recommend putting the ice in the glass first, but if you're really talented try putting it in last (tip: submerge the rim of the cup before squeezing the ice out).</li>
    <li>Enjoy the flavor experience of Quorvel. As the ice melts the flavor of your beverage slowly changes for a truly unique and ice cold experience!</li>
  </ul>
</main>
</body>
</html>
```